The billboard should communicate confidence, energy and approachability while maintaining a professional, premium feel. Rather than relying on a standard agent photograph, property collage or crowded list of services, we would like an original creative idea that makes people look twice. This could involve a fun visual, clever headline, striking colour contrast or an unexpected real estate theme. The concept should feel positive and contemporary, with enough personality to become recognisable throughout the local community.

The key message should appeal to homeowners who are thinking about selling, preparing to sell or simply curious about the value of their property. Copy must be short, clear and conversational, supported by a direct call to action. The agent’s name, phone number and company branding should remain highly visible without competing with the main idea.

The finished billboard will measure 8.0 metres wide by 2.08 metres high (1224px x 324px), so the composition must suit a long landscape format. All important text and imagery should remain comfortably within safe margins and be legible from a distance. The design should avoid small writing, unnecessary detail and visual clutter.

The goal is to create a billboard that feels different from every other real estate sign in the area—something engaging, confident and easy to remember. It should build strong brand awareness, generate conversations and encourage local property owners to contact the agent when they are ready to make their next move. The concept should be adaptable for future campaigns, helping establish a consistent, distinctive and trusted local brand presence.

Target Market(s)

ages 30+

Industry/Entity Type

Real Estate

Requirements
Must have
• call Colin and phone number 0437 15 82 63
Nice to have
• Nice bright and yellow.. Exciting and grabbing

```html
<!DOCTYPE html>
<html lang="en">
<head>
<meta charset="utf-8">
<title>Dale Forsyth – Next Move Billboard</title>
<link rel="stylesheet" href="https://fonts.googleapis.com/css2?family=Poppins:wght@400;700;800&display=swap">
<style>
  :root {
    --yellow: #ffe30f;
    --yellow-deep: #ffd400;
    --ink: #3b3b3a;
    --paper: #ffffff;
    --card: #c9a262;
    --card-light: #ddbb7e;
    --shade-top: #7a7a78;
    --shade-bottom: #4e4e4e;
  }
  * { margin: 0; padding: 0; box-sizing: border-box; }
  html, body {
    width: 1200px; height: 1184px; overflow: hidden;
    background: var(--paper);
  }
  .billboard {
    position: absolute; left: 50px; top: 448px;
    width: 1100px; height: 287px; overflow: hidden;
    background: linear-gradient(100deg, var(--yellow) 0%, var(--yellow) 55%, var(--yellow-deep) 100%);
    color: var(--ink);
    font-family: "Poppins", sans-serif;
  }
  .corner-shade { position: absolute; right: 0; top: 0; width: 97px; height: 177px; }
  .hero-visual {
    position: absolute; left: 703px; top: 60px; width: 397px; height: 227px;
    background:
      radial-gradient(closest-side at 62% 52%, var(--card-light) 0%, var(--card) 45%, rgba(201,162,98,0.55) 70%, rgba(255,214,0,0) 100%);
  }
  .headline {
    position: absolute; left: 58px; top: 22px;
    font-weight: 800;
    font-size: 58px; line-height: 66px; letter-spacing: -1px;
  }
  .headline-line { display: block; white-space: nowrap; }
  .brush-underline { position: absolute; left: 385px; top: 163px; width: 228px; height: 12px; }
  .call-to-action { position: absolute; left: 58px; top: 197px; display: flex; align-items: center; gap: 18px; }
  .phone-icon { width: 56px; height: 56px; flex: none; }
  .contact-label {
    font-weight: 400; font-size: 18px; line-height: 20px; display: block;
  }
  .contact-number {
    font-weight: 700; font-size: 42px; line-height: 42px; letter-spacing: -0.5px; display: block;
  }
  .brand-name {
    position: absolute; left: 676px; top: 38px;
    font-weight: 700; font-size: 28px; letter-spacing: -0.5px;
  }
  .tagline {
    position: absolute; right: 26px; top: 240px; text-align: right;
    font-weight: 400; font-size: 16px; line-height: 19px;
  }
</style>
</head>
<body>
  <section class="billboard" aria-label="Dale Forsyth billboard">
    <svg class="corner-shade" viewBox="0 0 97 177" preserveAspectRatio="none" aria-hidden="true">
      <defs>
        <linearGradient id="shade" x1="0" y1="0" x2="1" y2="1">
          <stop offset="0" stop-color="var(--shade-top)"/>
          <stop offset="1" stop-color="var(--shade-bottom)"/>
        </linearGradient>
      </defs>
      <polygon points="0,0 97,0 97,177" fill="url(#shade)"/>
    </svg>

    <div class="hero-visual" role="img" aria-label="Cardboard moving box folded into a house shape at the end of a winding white path"></div>

    <h1 class="headline">
      <span class="headline-line">Reasy to make</span>
      <span class="headline-line">your next move?</span>
    </h1>
    <svg class="brush-underline" viewBox="0 0 228 12" preserveAspectRatio="none" aria-hidden="true">
      <path d="M2 9 C60 3 150 1 226 6 L225 8 C150 5 70 7 3 11 Z" fill="var(--paper)"/>
    </svg>

    <div class="call-to-action">
      <svg class="phone-icon" viewBox="0 0 56 56" aria-hidden="true">
        <circle cx="28" cy="28" r="28" fill="var(--ink)"/>
        <path d="M18 17c2-2 4-2 5 0l3 5c1 2 0 3-1 4l-1 1c1 3 4 6 7 7l1-1c1-1 2-2 4-1l5 3c2 1 2 3 0 5l-2 2c-3 2-8 0-13-5s-7-10-5-13z" fill="var(--yellow)"/>
        <path d="M30 19a7 7 0 0 1 7 7M31 14a12 12 0 0 1 11 11M32 9a17 17 0 0 1 15 15" stroke="var(--yellow)" stroke-width="2.4" fill="none" stroke-linecap="round"/>
      </svg>
      <div class="contact">
        <span class="contact-label">Call Colin</span>
        <span class="contact-number">0437 15 82 63</span>
      </div>
    </div>

    <div class="brand-name">Dale Forsyth</div>

    <p class="tagline">MORE<br>THAN A MOVE.</p>
  </section>
</body>
</html>
```